Redesign of the Klammbrot label

I am a pharmacist and sell a bitters called "Klammbrot". I would like to revise and modernize the current logo of my "Klammbrot". I have attached a photo of the current label. I have different bottle sizes with different label sizes, but for now I will only need one label for the 700ml size:
20ml 36x47mm
40ml 45x62mm
200ml 70x91mm
350ml 70x98mm
500ml 70x110mm
700ml 87x119mm
The Uffe is a small stream that runs through our town. The Klammbrot is a play on words that takes up the mysticism of the Harz, as a spirit can of course also be a schnapps. I like the mysticism and rough nature of the Harz in connection with the product. I have attached a logo suggestion that I once had an AI design. But I am very open to new ideas. A connection to my pharmacy does not necessarily have to be recognizable. VG, K. Brandis

Target Market(s)

End consumers, gastronomy, restaurants, hotels

```html
<!DOCTYPE html>
<html lang="de">
<head>
<meta charset="utf-8">
<title>Klammbrot Bitterlikör – Etikett 700 ml</title>
<link rel="stylesheet" href="https://fonts.googleapis.com/css2?family=Libre+Baskerville:ital,wght@0,400;0,700;1,400&family=Old+Standard+TT:wght@700&display=swap">
<style>
  :root {
    --cream: #ebe7dc;
    --ochre: #a2723c;
    --brown: #86602f;
    --forest: #5e4724;
    --dark: #372a17;
    --ink: #1a130b;
    --title-brown: #4d3b1a;
    --gold: #9b6a2f;
    --wine: #a3223a;
    --dot: #c9c3b8;
    --white: #ffffff;
  }
  * { margin: 0; padding: 0; box-sizing: border-box; }
  html, body { width: 1200px; height: 927px; overflow: hidden; background: var(--white); }
  body { position: relative; font-family: "Libre Baskerville", Georgia, serif; }

  .label {
    position: absolute; left: 330px; top: 111px; width: 539px; height: 704px;
    border-radius: 9px; overflow: hidden;
    box-shadow: 0 2px 8px rgba(0,0,0,.35);
  }
  .label__scene {
    position: absolute; inset: 0;
    background: linear-gradient(to bottom,
      var(--cream) 0%, var(--cream) 14%,
      var(--ochre) 19%, var(--ochre) 40%,
      var(--brown) 46%, var(--brown) 60%,
      var(--forest) 70%, var(--dark) 82%, var(--dark) 100%);
  }
  .arc { position: absolute; left: 0; top: 0; width: 539px; }
  .origin {
    position: absolute; left: 0; width: 100%; top: 82px; text-align: center;
    font: 700 16px "Libre Baskerville", Georgia, serif; color: var(--gold);
  }
  .product-name {
    position: absolute; left: 0; width: 100%; top: 160px; text-align: center;
    font: 700 62px/1 "Old Standard TT", "Times New Roman", serif; color: var(--ink);
    letter-spacing: -1px; white-space: nowrap;
    transform: scaleY(1.35); transform-origin: 50% 0;
    text-shadow: 0 0 2px #e6a866, 0 0 4px #d89050;
  }
  .category {
    position: absolute; left: 0; width: 100%; top: 252px; text-align: center;
    font: 700 24px "Libre Baskerville", Georgia, serif; color: var(--white);
  }
  .rule { position: absolute; height: 1px; }
  .rule--category { left: 150px; width: 240px; top: 284px; background: var(--dark); }
  .rule--story { left: 180px; width: 200px; top: 467px; background: var(--gold); }
  .story {
    position: absolute; left: 30px; width: 479px; top: 384px; text-align: center;
    font: italic 400 13px/16.2px "Libre Baskerville", Georgia, serif; color: var(--white);
    letter-spacing: .5px;
  }
  .info {
    position: absolute; left: 37px; top: 492px; width: 469px; height: 163px;
    background: var(--white);
    border-top: 3px dotted var(--dark); border-bottom: 3px dotted var(--dark);
  }
  .info__frame {
    position: absolute; left: 28px; top: 16px; width: 412px; height: 124px;
    border-top: 2px dotted var(--dot); border-bottom: 2px dotted var(--dot);
  }
  .info__divider {
    position: absolute; left: 280px; top: 27px; height: 100px;
    border-left: 2px dotted var(--dot);
  }
  .info__subdivider {
    position: absolute; left: 292px; top: 84px; width: 148px;
    border-top: 2px dotted var(--dot);
  }
  .maker p { position: absolute; white-space: nowrap; }
  .maker__intro { left: 33px; top: 20px; font: italic 400 12px/1 "Libre Baskerville", Georgia, serif; color: var(--wine); }
  .maker__name { left: 30px; top: 37px; font: 400 17px/1 "Libre Baskerville", Georgia, serif; color: var(--ink); }
  .maker__town { left: 29px; top: 56px; font: 400 20px/1 "Libre Baskerville", Georgia, serif; color: var(--wine); }
  .maker__person { left: 32px; top: 81px; font: italic 400 13.5px/1 "Libre Baskerville", Georgia, serif; color: var(--ink); }
  .maker__address { left: 32px; top: 97px; font: italic 400 11.5px/13.5px "Libre Baskerville", Georgia, serif; color: var(--wine); }
  .herb {
    position: absolute; left: 298px; top: 31px; width: 136px; height: 47px;
    background: linear-gradient(160deg, #c9a06a, #9b6a2f);
    border-radius: 50% 10% 50% 40%;
  }
  .volume {
    position: absolute; left: 290px; top: 92px; width: 150px; text-align: center;
    font: italic 400 36px/1 "Libre Baskerville", Georgia, serif; color: var(--wine);
  }
  .abv {
    position: absolute; left: 290px; top: 126px; width: 150px; text-align: center;
    font: 400 12.5px/1 "Libre Baskerville", Georgia, serif; color: var(--ink);
  }
</style>
</head>
<body>
  <main class="label">
    <div class="label__scene" role="img" aria-label="Harz landscape: layered mountain ridges under a pale sky with birds, fading into a dark fir forest"></div>

    <svg class="arc" viewBox="0 0 539 340" height="340">
      <defs>
        <path id="arc-origin" d="M120 100 Q270 50 420 100"/>
        <path id="arc-tagline" d="M95 296 Q270 340 445 290"/>
      </defs>
      <rect x="110" y="88" width="7" height="7" fill="#000" transform="rotate(-20 113 91)"/>
      <rect x="424" y="88" width="7" height="7" fill="#000" transform="rotate(20 427 91)"/>
      <text font-family="Libre Baskerville, Georgia, serif" font-weight="700" font-size="26" fill="var(--title-brown)" text-anchor="middle">
        <textPath href="#arc-origin" startOffset="50%">BAD TANNFELDER</textPath>
      </text>
      <circle cx="101" cy="290" r="1.6" fill="var(--dark)"/>
      <circle cx="450" cy="290" r="1.6" fill="var(--dark)"/>
      <text font-family="Libre Baskerville, Georgia, serif" font-style="italic" font-size="18" fill="var(--dark)" text-anchor="middle">
        <textPath href="#arc-tagline" startOffset="50%">NACH ALTER APOTHEKERKUNST</textPath>
      </text>
    </svg>

    <p class="origin">ERLESENER</p>
    <h1 class="product-name">KLAMMBROT</h1>
    <p class="category">BITTERLIKOR</p>
    <div class="rule rule--category"></div>

    <p class="story">Eine Zubereitung nach höchst geheimem Rezept. Sie sei<br>empfohlen zum Genuss nach einem guten Mahl.<br>Aufs Feinste zubereitet mit geistigen Auszügen von Enzian,<br>Kalmus, Malabar-Kardamom und anderen wertvollen Zutaen.</p>
    <div class="rule rule--story"></div>

    <section class="info">
      <div class="info__frame"></div>
      <div class="info__divider"></div>
      <div class="info__subdivider"></div>
      <div class="maker">
        <p class="maker__intro">Aus der</p>
        <p class="maker__name">ST. LORENZ APOTHEKE</p>
        <p class="maker__town">Bad Tannfeld</p>
        <p class="maker__person">Dr. K. Brandis</p>
        <p class="maker__address">Lindenweg 12<br>37449 Bad Tannfeld<br>Tel. 05500-1234</p>
      </div>
      <div class="herb" role="img" aria-label="Engraved botanical leaf illustration"></div>
      <p class="volume">700ML</p>
      <p class="abv">34% VOL</p>
    </section>
  </main>
</body>
</html>
```